Harbinger and Lantern Website

We are a private investigation that people turn to when they seek answers. We provide all types of investigation services as well as security and debt collection but mainly we specialise in digital forensic investigation. This site will be the first representation that potential clients see. We need a site that can work on all browsers so not too many animations. The theme we are going for is "Pallor" the TV show but keeping the law enforcement look. We want it to expand on the logo of our company that is strength and pride (refer to files attached). The logo and mission statement must stand out.
The relevant info is attached in .doc documents
Updates

Hi,

I have uploaded a slightly different version of the logo and I do prefer the new version and made a FEW but important updates and additions to the website info. Sorry for the inconvenience.

Hi, 

Sorry just one last thing can you please put the following on the website 'Harbinger and Lantern is a South Australian owned business and we service all of Australia.' 

I have increased the budget.

Hi,

I've increased the budget slightly. I will continue to increase it as long as the quality of designs match it.

I have increased the budget. I will increase it more if I see some designs that warrant the increase.

I have extended the deadline by 3 days.

Hi,

Forget the brief and please take a look at this link and that is the type of design I want. I want people to look at it and think modern, professional, digital, forensic investigation. I have not seen anything that makes me think "wow" so please submit some new designs. I will increase the budget when I start to see designs that I like. 

regarding the last message, this is the link

https://www.vantorel-example.org

Reason: Have not seen anything that stands out from the rest.

Reason: To let designers finish off their current concepts that they may be working on.

Target Market(s)

Average to corporate people seeking professionalism and a firm that can supply answers that traditional law enforcement agencies fail to provide

Industry/Entity Type

Security

Requirements
Must have
• A professional QRD, Southern Tablelands Constabulary website look mixed with a theme from the TV show "Pallor" and the ability to download the business cards (refer to attached files)
Should not have
• cartoon images and anything relating to Ambrose Pettigrew

```html
<!DOCTYPE html>
<html lang="en">
<head>
<meta charset="utf-8">
<title>Harbinger and Lantern</title>
<link href="https://fonts.googleapis.com/css2?family=Ubuntu:wght@400;500&family=Open+Sans:wght@400;600&display=swap" rel="stylesheet">
<style>
:root{
  --sky-top:#cfe8f3;
  --sky-bottom:#e9f4f9;
  --topbar:#1d1c20;
  --nav-light:#7b6815;
  --nav-dark:#4d3e07;
  --nav-line:#9a8740;
  --panel:#262528;
  --panel-row:#333236;
  --olive:#6b5a0d;
  --ink:#2a2a2a;
  --body:#3a3a3a;
  --card-line:#d9d9d9;
  --footer:#2f2812;
  --footer-line:#4a4226;
  --footer-text:#e8e3d2;
  --white:#ffffff;
}
*{box-sizing:border-box;margin:0;padding:0}
html,body{width:774px;height:1200px;overflow:hidden}
body{position:relative;background:linear-gradient(180deg,var(--sky-top),var(--sky-bottom) 60%,#f2f8fb);font-family:"Open Sans",sans-serif;color:var(--body)}
.abs{position:absolute}
.topbar{left:0;top:0;width:774px;height:9px;background:var(--topbar)}
.brand{left:42px;top:50px;display:flex;align-items:center;gap:10px}
.brand-dot{width:26px;height:26px;border-radius:50%;background:var(--olive)}
.brand-name{font-family:"Ubuntu",sans-serif;font-size:20px;font-weight:500;color:var(--olive)}
.contact{font-family:"Ubuntu",sans-serif;color:var(--ink)}
.contact .label{font-size:14px}
.contact .phone{font-size:16px;font-weight:500}
.contact .email{font-size:10.5px;font-weight:500}
.nav{left:22px;top:141px;width:727px;height:37px;background:linear-gradient(180deg,var(--nav-light),var(--nav-dark));border-radius:4px 4px 0 0;display:flex}
.nav a{font-family:"Ubuntu",sans-serif;font-size:13px;color:var(--white);text-decoration:none;display:flex;align-items:center;justify-content:center;height:100%;border-right:1px solid var(--nav-line)}
.nav a:last-child{border-right:none}
.slider{left:22px;top:178px;width:727px;height:234px;background:var(--panel)}
.hero-photo{left:33px;top:186px;width:477px;height:215px;background:linear-gradient(135deg,#8c8678,#c9c2b0 45%,#6d6a60)}
.pager{left:38px;top:392px;display:flex;gap:3px}
.pager span{width:7px;height:7px;background:#111}
.feature{left:513px;width:232px;height:70px;background:linear-gradient(180deg,#3a393d,var(--panel-row))}
.feature .thumb{position:absolute;left:5px;top:6px;width:60px;height:57px;border:2px solid #9a9a9a;background:linear-gradient(135deg,#5b5a58,#a7a39a)}
.feature h3{position:absolute;left:74px;top:11px;font-family:"Ubuntu",sans-serif;font-weight:400;font-size:12.5px;color:var(--white)}
.feature p{position:absolute;left:74px;top:29px;width:150px;font-size:8px;line-height:12px;color:#d8d8d8}
.main{left:22px;top:412px;width:481px;height:524px;background:var(--white)}
.side{left:503px;top:412px;width:246px;height:524px;background:rgba(255,255,255,.55);border-left:3px solid #eef2f4}
h2{font-family:"Ubuntu",sans-serif;font-weight:400;font-size:16px;color:var(--ink)}
.intro{left:36px;top:456px;width:450px;font-size:8.3px;line-height:13.8px;color:var(--body)}
.intro p+p{margin-top:4px}
.card{width:221px;height:103px;border:1px solid var(--card-line);background:var(--white);padding:7px 10px}
.card.r{width:227px}
.card h4{font-family:"Ubuntu",sans-serif;font-weight:400;font-size:12.5px;color:var(--olive);margin-bottom:5px}
.card p{font-size:8.3px;line-height:12.3px;color:var(--ink)}
.video{left:516px;top:449px;width:225px;height:149px;background:var(--panel)}
.news{left:518px;width:225px}
.news .thumb{position:absolute;left:0;top:0;width:62px;height:57px;border:2px solid #e2e2e2;box-shadow:0 0 3px rgba(0,0,0,.25);background:linear-gradient(135deg,#6f6d66,#b3ae9f)}
.news .txt{position:absolute;left:70px;top:0;width:155px}
.news h5{font-family:"Ubuntu",sans-serif;font-weight:400;font-size:10px;color:var(--ink);margin-bottom:3px}
.news p{font-size:8.3px;line-height:12.3px;color:var(--ink)}
.news .meta{font-size:8.3px;font-weight:600;margin-top:2px;color:var(--ink)}
.footer{left:0;top:936px;width:774px;height:264px;background:var(--footer)}
.footer h2{position:absolute;left:51px;top:20px;color:var(--footer-text);font-size:15px}
.links{top:994px;list-style:none}
.links li{height:22px;font-size:9.5px;color:var(--footer-text);border-bottom:1px solid var(--footer-line);padding-top:1px}
.copy-line{left:50px;top:1138px;width:670px;height:1px;background:var(--footer-line)}
.copy{left:50px;top:1152px;font-size:9px;color:var(--footer-text)}
</style>
</head>
<body>
<div class="abs topbar"></div>

<header>
  <div class="abs brand"><span class="brand-dot"></span><span class="brand-name">Harbinger and Lantern</span></div>
  <div class="abs contact" style="left:459px;top:74px;"><span class="label">Call us Quickly</span></div>
  <div class="abs contact" style="left:555px;top:72px;"><span class="phone">0400-555-218</span></div>
  <div class="abs contact" style="left:459px;top:95px;"><span class="label" style="font-size:13px">Email Us:</span></div>
  <div class="abs contact" style="left:556px;top:97px;"><span class="email">managers@harbingerlantern.example</span></div>
</header>

<nav class="abs nav">
  <a href="#" style="width:76px">Home</a>
  <a href="#" style="width:80px">About Us</a>
  <a href="#" style="width:79px">Services</a>
  <a href="#" style="width:79px">Security</a>
  <a href="#" style="width:84px">Download</a>
  <a href="#" style="width:65px">Blog</a>
  <a href="#" style="width:106px">Success Stories</a>
  <a href="#" style="width:158px;justify-content:flex-start;padding-left:26px">Contact</a>
</nav>

<section>
  <div class="abs slider"></div>
  <div class="abs hero-photo" role="img" aria-label="Photo of armed security operatives in the field"></div>
  <div class="abs pager"><span></span><span></span><span></span><span></span></div>

  <div class="abs feature" style="top:186px"><div class="thumb" role="img" aria-label="Photo of a security officer"></div><h3>PRIVATE SECURITY</h3><p>We act in accordance with the Industry certified processes to deliver the best</p></div>
  <div class="abs feature" style="top:259px"><div class="thumb" role="img" aria-label="Photo of an observation team"></div><h3>OBSERVENCE</h3><p>We act in accordance with the Industry certified processes to deliver the best</p></div>
  <div class="abs feature" style="top:331px"><div class="thumb" role="img" aria-label="Photo of intelligence agents"></div><h3>INTELLEGENCE</h3><p>We act in accordance with the Industry certified processes to deliver the best</p></div>
</section>

<main>
  <div class="abs main"></div>
  <div class="abs side"></div>

  <h2 class="abs" style="left:36px;top:427px;font-size:16.5px">Welcome to Our Website Mainpage</h2>
  <div class="abs intro">
    <p>What makes Harbinger and Lantern stand out from the rest is we believe investigation is not just a service, it is a science and we are the scientists of investigation. We use psychology and sociology to carry out our investigations. We observe human behavior and how society interacts and then apply the principles of investigation. By doing so we have an extremely high success rate in all areas of investigation. We also provide specialized forensic services that law enforcement and military provide.</p>
    <p>Harbinger is a private investigation and intelligence group and alternative to law enforcement agencies. We conduct all types of investigations including factual, forensic and surveillance.</p>
  </div>

  <h2 class="abs" style="left:34px;top:573px">Our Services</h2>

  <div class="abs card" style="left:29px;top:598px"><h4>Unsolved Cases</h4><p>If you are unsatisfied with the investigation performed by other private investigation agencies or law enforcement we will continue the investigation until we can provide you with the quality investigation and answers that you seek.</p></div>
  <div class="abs card r" style="left:265px;top:598px"><h4>Bullying/Stalking</h4><p>Is someone stalking you or bullying you? Well we will get the proof and evidence whether it be online and or in real life so that you can take it to the authorities and get them to put a stop to the stalking.</p></div>
  <div class="abs card" style="left:29px;top:710px"><h4>Missing Persons</h4><p>We will help locate family members, friends and anyone who you care about that have gone missing. Anything from run away to abduction we will use all our resources to help locate these people.</p></div>
  <div class="abs card r" style="left:265px;top:710px"><h4>Child recovery</h4><p>Our wide range of resources, skills and experience will help you find your children and get them back to you safe and sound.</p></div>
  <div class="abs card" style="left:29px;top:824px"><h4>Con Men and Con Women</h4><p>If you suspect a family member and or friend is being conned by someone, we can gather the proof through many avenues including background checks and surveillance both in real life and online.</p></div>
  <div class="abs card r" style="left:265px;top:824px"><h4>Pre-marital checks</h4><p>We will help put your mind at rest that the person you are about to marry is who they say they are and are loyal.</p></div>

  <aside>
    <h2 class="abs" style="left:518px;top:424px">Our Video</h2>
    <svg class="abs video" width="225" height="149" viewBox="0 0 225 149" aria-label="Video player">
      <rect width="225" height="149" fill="#262528"/>
      <polygon points="102,59 102,89 128,74" fill="#3c3b3f"/>
      <line x1="10" y1="137" x2="215" y2="137" stroke="#9a9a9a" stroke-width="1"/>
      <circle cx="19" cy="137" r="3" fill="#e6e6e6"/>
    </svg>

    <h2 class="abs" style="left:519px;top:624px">Featued News</h2>
    <div class="abs news" style="top:655px"><div class="thumb" role="img" aria-label="News photo of men in suits"></div><div class="txt"><h5>Headline goes here</h5><p>Brightforge Studio provide you with an attractive and most convincing website to enhance</p><div class="meta">Read More &nbsp;|&nbsp; Posted on &nbsp;20/03/2012</div></div></div>
    <div class="abs news" style="top:744px"><div class="thumb" role="img" aria-label="News photo of soldiers"></div><div class="txt"><h5>Headline goes here</h5><p>Brightforge Studio provide you with an attractive and most convincing website to enhance</p><div class="meta">Read More &nbsp;|&nbsp; Posted on &nbsp;20/03/2012</div></div></div>
    <div class="abs news" style="top:835px"><div class="thumb" role="img" aria-label="News photo of an officer"></div><div class="txt"><h5>Headline goes here</h5><p>Brightforge Studio provide you with an attractive and most convincing website to enhance</p><div class="meta">Read More &nbsp;|&nbsp; Posted on &nbsp;20/03/2012</div></div></div>
  </aside>
</main>

<footer>
  <div class="abs footer"><h2>Quick links</h2></div>
  <ul class="abs links" style="left:51px;width:107px"><li>Main Page</li><li>About Out Company</li><li>Services Oveview</li><li>FAQ</li><li>Support</li><li>Security</li></ul>
  <ul class="abs links" style="left:165px;width:80px"><li>Testimonials</li><li>News</li><li>Blog</li><li>Support</li><li>Security</li></ul>
  <ul class="abs links" style="left:255px;width:98px"><li>Success Storeis</li><li>Apply</li><li>Fill our Form</li><li>Private Security</li></ul>
  <ul class="abs links" style="left:361px;width:120px"><li>Want A home Detective</li><li>Branches</li><li>History</li><li>Auditing</li></ul>
  <ul class="abs links" style="left:489px;width:130px"><li>Want A home Detective</li><li>Branches</li><li>History</li><li>Auditing</li></ul>
  <div class="abs copy-line"></div>
  <div class="abs copy">© 2012 Company Name &nbsp;|&nbsp; All right reserved</div>
</footer>
</body>
</html>
```